Redesign of business card for Alderstone Mechanical

We are looking for a new design for our business cards for Alderstone Mechanical. We are a plumbing & HVAC construction company, operating on the West Coast of Canada and USA. Logo attached.
Updates
Need extra days to review
Gathering more feedback
Industry/Entity Type
Construction - Plumbing & HVAC
Contact Information for Business Card
Name, address, phone numbers, email, website address
Look and feel
Each slider illustrates characteristics of the customer's brand and the style your logo design should communicate.

```html
<!DOCTYPE html>
<html lang="en">
<head>
<meta charset="utf-8">
<title>Alderstone Mechanical – Business Card</title>
<link href="https://fonts.googleapis.com/css2?family=Montserrat:wght@400;700&display=swap" rel="stylesheet">
<style>
  :root {
    --page-bg: #1a1a1a;
    --card-white: #ffffff;
    --card-dark: #262626;
    --ink: #1f1f1f;
    --ink-soft: #3a3a3a;
    --on-dark: #f2f2f2;
  }
  * { margin: 0; padding: 0; box-sizing: border-box; }
  html, body {
    width: 1200px; height: 1059px; overflow: hidden;
    background: var(--page-bg);
    font-family: "Montserrat", sans-serif;
  }
  .card {
    position: absolute; left: 253px;
    width: 692px; height: 393px;
    border-radius: 22px; overflow: hidden;
  }
  .card--front { top: 89px; background: var(--card-white); }
  .card--back { top: 546px; background: var(--card-dark); }

  .wave { position: absolute; inset: 0; width: 100%; height: 100%; }

  .accent-bar {
    position: absolute; left: 0; top: 56px;
    width: 16px; height: 42px; background: var(--card-dark);
  }
  .person { position: absolute; left: 38px; top: 52px; color: var(--ink); }
  .person__name { font-weight: 700; font-size: 23px; letter-spacing: 0.5px; }
  .person__title { font-size: 14px; color: var(--ink-soft); margin-top: 2px; letter-spacing: 0.3px; }

  .brand {
    position: absolute; display: flex; align-items: center; gap: 12px;
    font-weight: 700; text-transform: uppercase; letter-spacing: 1px; line-height: 1.15;
  }
  .brand__mark { flex: none; }
  .brand--front { left: 420px; top: 108px; color: var(--ink); font-size: 21px; }
  .brand--front .brand__mark { width: 26px; height: 26px; background: var(--ink); }
  .brand--back { left: 0; right: 0; top: 158px; justify-content: center; color: var(--on-dark); font-size: 32px; }
  .brand--back .brand__mark { width: 36px; height: 36px; background: var(--on-dark); }

  .contact { position: absolute; left: 32px; top: 227px; color: var(--on-dark); font-size: 14.5px; }
  .contact__address { line-height: 18px; margin-bottom: 20px; }
  .contact__row { display: flex; align-items: center; gap: 10px; height: 27px; }
  .contact__icon { width: 13px; height: 13px; fill: var(--on-dark); flex: none; }
</style>
</head>
<body>
  <section class="card card--front">
    <svg class="wave" viewBox="0 0 692 393" preserveAspectRatio="none" aria-hidden="true">
      <path d="M0 193 C40 170 80 158 120 158 C230 158 320 230 420 285 C520 335 620 285 692 237 L692 393 L0 393 Z" fill="var(--card-dark)"/>
      <path d="M0 240 C40 215 80 205 115 205 C210 205 290 270 380 318 C470 362 600 340 692 281 L692 290 C600 352 470 372 375 326 C290 282 210 212 115 212 C80 212 40 222 0 248 Z" fill="var(--card-white)"/>
      <path d="M175 210 C270 225 340 290 430 330 C460 342 490 348 512 350 C480 348 455 340 425 326 C340 286 265 226 175 210 Z" fill="var(--card-white)"/>
    </svg>
    <div class="accent-bar"></div>
    <div class="person">
      <div class="person__name">Daniel Reyes</div>
      <div class="person__title">Managing Director</div>
    </div>
    <div class="brand brand--front">
      <span class="brand__mark"></span>
      <span>Alderstone<br>Mechanical</span>
    </div>
    <div class="contact">
      <div class="contact__address">48 Cedar Ridge Road<br>Portland, OR 97205</div>
      <div class="contact__row">
        <svg class="contact__icon" viewBox="0 0 24 24"><path d="M6.6 10.8a15.1 15.1 0 0 0 6.6 6.6l2.2-2.2c.3-.3.7-.4 1-.2 1.1.4 2.3.6 3.6.6.6 0 1 .4 1 1V20c0 .6-.4 1-1 1A17 17 0 0 1 3 4c0-.6.4-1 1-1h3.5c.6 0 1 .4 1 1 0 1.3.2 2.5.6 3.6.1.3 0 .7-.2 1z"/></svg>
        <span>555.014.2290</span>
      </div>
      <div class="contact__row">
        <svg class="contact__icon" viewBox="0 0 24 24"><path d="M2 5h20v14H2z M2 5l10 8 10-8" fill="var(--on-dark)"/><path d="M3 6l9 7 9-7" fill="none" stroke="var(--card-dark)" stroke-width="1.8"/></svg>
        <span>info@alderstonemechanical.com</span>
      </div>
      <div class="contact__row">
        <svg class="contact__icon" viewBox="0 0 24 24"><circle cx="12" cy="12" r="10"/><path d="M2 12h20M12 2c3 3 3 17 0 20M12 2c-3 3-3 17 0 20" fill="none" stroke="var(--card-dark)" stroke-width="1.5"/></svg>
        <span>www.alderstonemechanical.com</span>
      </div>
    </div>
  </section>

  <section class="card card--back">
    <div class="brand brand--back">
      <span class="brand__mark"></span>
      <span>Alderstone Mechanical</span>
    </div>
  </section>
</body>
</html>
```